Power point design for a financial seminar

I would like to receive 10 designed power point slides with the same look & feel that should related to finance since its for a seminar related to stock markets and economics. Please note that texts are in Hebrew (translate is attached in a Word document).
There should be background with upper and bottom layers similar to all to include the attached logo.
All slides should have a Title and some of the slides should have designed bullets and other generic graphic elements that we will use in our presentation.
Please note that text should be right to left so texts will be aligned to the right and graphics at the left/upper/bottom
Target Market(s)
Youngsters
Look and feel
Each slider illustrates characteristics of the customer's brand and the style your logo design should communicate.

```html
<!DOCTYPE html>
<html lang="he" dir="rtl">
<head>
<meta charset="utf-8">
<title>קורס שוק ההון - מצגת</title>
<link href="https://fonts.googleapis.com/css2?family=Heebo:wght@400;500;700;800&display=swap" rel="stylesheet">
<style>
:root{
  --page:#ffffff;
  --ink:#1b2a3a;
  --muted:#5b6673;
  --blue-deep:#0a55a6;
  --blue:#1c7bd1;
  --blue-light:#5fb0ea;
  --blue-pale:#dcebf8;
  --teal:#3cbfa3;
  --line:#e3e9f0;
  --card-num:#e6edf5;
}
*{margin:0;padding:0;box-sizing:border-box}
html,body{width:1200px;height:2400px;overflow:hidden;background:var(--page)}
body{position:relative;font-family:'Heebo',sans-serif;color:var(--ink)}

.slide{position:absolute;width:540px;height:304px;background:#fff;overflow:hidden;direction:rtl;
  transform-origin:top left;box-shadow:0 8px 22px rgba(20,40,70,.22)}
.slide-rule{position:absolute;left:0;right:0;bottom:6px;height:2px;background:linear-gradient(90deg,var(--blue-deep),var(--blue-light))}
.slide-mark{position:absolute;left:12px;bottom:12px;width:16px;height:16px;border-radius:50%;background:var(--blue-pale);border:2px solid var(--teal)}
.slide-num{position:absolute;left:36px;bottom:12px;font-size:8px;color:var(--muted)}

/* collage */
.collage{position:absolute;left:0;top:0;width:1200px;height:1150px;transform:rotate(-7deg);transform-origin:600px 575px}
.c-securities{left:560px;top:120px;transform:scale(1.25)}
.c-lecturer{left:-330px;top:230px;transform:scale(1.25)}
.c-exchange{left:-90px;top:700px;transform:scale(1.25)}
.c-indices{left:690px;top:540px;transform:scale(1.25)}
.c-hero{left:130px;top:300px;transform:scale(1.7);box-shadow:0 10px 26px rgba(20,40,70,.3)}

/* grid */
.g1{left:106px;top:1212px;transform:scale(.854)}
.g2{left:630px;top:1212px;transform:scale(.854)}
.g3{left:106px;top:1547px;transform:scale(.854)}
.g4{left:630px;top:1547px;transform:scale(.854)}
.g5{left:368px;top:1879px;transform:scale(.854)}

/* title slide */
.title-slide{background:linear-gradient(180deg,var(--blue-deep),var(--blue) 60%,var(--blue-light))}
.title-slide .market-photo{position:absolute;inset:0;background:linear-gradient(160deg,rgba(255,255,255,.08),rgba(10,60,130,.25) 55%,rgba(255,255,255,.12))}
.brand-tab{position:absolute;top:0;left:185px;width:170px;height:82px;background:var(--blue-pale);
  border-radius:0 0 16px 16px;text-align:center;padding-top:8px}
.brand-dot{width:26px;height:26px;border-radius:50%;background:var(--teal);margin:0 auto 4px}
.brand-name{font-size:13px;font-weight:800;color:var(--ink);line-height:1.1}
.brand-sub{font-size:10px;font-weight:800;color:var(--ink);line-height:1.2}
.course-title{position:absolute;top:118px;left:0;right:0;text-align:center;color:#fff;font-size:29px;font-weight:800}
.presenter-pill{position:absolute;top:182px;left:185px;width:170px;height:30px;border-radius:15px;
  background:var(--teal);color:#fff;font-size:14px;font-weight:500;text-align:center;line-height:30px}

/* lecturer */
.side-panel{position:absolute;top:0;right:0;width:130px;height:290px;background:linear-gradient(180deg,var(--blue-light),var(--blue) 55%,var(--blue-deep))}
.side-panel .portrait{position:absolute;right:40px;bottom:0;width:80px;height:170px;border-radius:40px 40px 0 0;background:linear-gradient(180deg,rgba(10,60,120,.35),rgba(10,60,120,.6))}
.panel-title{position:absolute;top:18px;right:14px;color:#fff;font-size:22px;font-weight:800;line-height:1.15}
.bio-list{position:absolute;top:28px;right:150px;width:360px;list-style:none}
.bio-list li{display:flex;align-items:center;gap:10px;height:44px;border-bottom:1px solid var(--line);font-size:11px;font-weight:500}
.bio-icon{width:18px;height:18px;border-radius:4px;background:var(--teal);flex:none;display:flex;align-items:center;justify-content:center}

/* exchange */
.top-band{position:absolute;top:0;left:0;right:0;height:82px;background:linear-gradient(90deg,var(--blue-light),var(--blue) 50%,var(--blue-deep))}
.band-title{position:absolute;top:12px;right:22px;color:#fff;font-size:20px;font-weight:800}
.topic-grid{position:absolute;top:58px;right:24px;left:24px;display:grid;grid-template-columns:repeat(3,1fr);gap:16px 18px}
.topic-card{position:relative;height:86px;background:#fff;box-shadow:0 3px 10px rgba(20,40,70,.18);padding:10px;font-size:10.5px;font-weight:500;line-height:1.35}
.topic-card .num{position:absolute;top:4px;left:8px;font-size:24px;font-weight:800;color:var(--card-num)}
.topic-card p{position:relative;margin-top:22px}

/* securities */
.center-title{position:absolute;top:14px;left:0;right:0;text-align:center;font-size:15px;font-weight:800}
.securities-chart{position:absolute;left:185px;top:60px}
.sec-label{position:absolute;font-size:11px;font-weight:500;padding-bottom:3px;border-bottom:1px solid var(--line);width:110px}

/* indices */
.curve-panel{position:absolute;top:0;right:0}
.curve-title{position:absolute;top:16px;right:22px;color:#fff;font-size:20px;font-weight:800}
.index-item{position:absolute;font-size:10.5px;font-weight:500;text-align:right;width:290px;line-height:1.3}
.chev{position:absolute;width:20px;height:20px;border-radius:50%;background:#fff;border:2px solid var(--blue-pale);display:flex;align-items:center;justify-content:center}
</style>
</head>
<body>

<div class="collage">
  <section class="slide c-securities">
    <h2 class="center-title">ני"ע נסחרים בבורסה</h2>
    <svg class="securities-chart" width="170" height="170" viewBox="-85 -85 170 170" aria-hidden="true">
      <g fill="var(--blue-deep)" stroke="#fff" stroke-width="3">
        <path d="M0,-80 A80,80 0 0 1 76.1,-24.7 L20.9,-6.8 A22,22 0 0 0 0,-22 Z"/>
        <path d="M76.1,-24.7 A80,80 0 0 1 47,64.7 L12.9,17.8 A22,22 0 0 0 20.9,-6.8 Z"/>
        <path d="M47,64.7 A80,80 0 0 1 -47,64.7 L-12.9,17.8 A22,22 0 0 0 12.9,17.8 Z"/>
        <path d="M-47,64.7 A80,80 0 0 1 -76.1,-24.7 L-20.9,-6.8 A22,22 0 0 0 -12.9,17.8 Z"/>
        <path d="M-76.1,-24.7 A80,80 0 0 1 0,-80 L0,-22 A22,22 0 0 0 -20.9,-6.8 Z"/>
      </g>
      <circle r="20" fill="#fff"/>
    </svg>
    <div class="sec-label" style="right:24px;top:70px">מניות</div>
    <div class="sec-label" style="right:24px;top:150px">אג"חים</div>
    <div class="sec-label" style="left:24px;top:70px;text-align:left">נגזרים פיננסים</div>
    <div class="slide-rule"></div><div class="slide-mark"></div>
  </section>

  <section class="slide c-lecturer">
    <div class="side-panel">
      <div class="portrait" role="img" aria-label="צללית של המרצה על רקע כחול"></div>
      <h2 class="panel-title">רקע על<br>המרצה</h2>
    </div>
    <ul class="bio-list">
      <li><span class="bio-icon"></span>בעל שני תארים במנהל עסקים</li>
      <li><span class="bio-icon"></span>מרצה במכללה לכלכלה</li>
      <li><span class="bio-icon"></span>יזם הייטק בתחום הפינטק</li>
      <li><span class="bio-icon"></span>כותב טורי דעה בנושאי כלכלה</li>
      <li><span class="bio-icon"></span>הקים וניהל חברה למסחר בנגזרים</li>
    </ul>
    <div class="slide-rule"></div><div class="slide-mark"></div>
  </section>

  <section class="slide c-exchange">
    <div class="top-band"><h2 class="band-title">בורסה</h2></div>
    <div class="topic-grid">
      <div class="topic-card"><span class="num">01</span><p>מה זו בורסה?</p></div>
      <div class="topic-card"><span class="num">02</span><p>ההיסטוריה של הבורסה</p></div>
      <div class="topic-card"><span class="num">03</span><p>הקבוצות הציבוריות והמוסדות</p></div>
      <div class="topic-card"><span class="num">04</span><p>ההבדל בין שוק ראשוני לשוק משני</p></div>
      <div class="topic-card"><span class="num">05</span><p>איך הבורסה משפיעה על הכלכלה?</p></div>
      <div class="topic-card"><span class="num">06</span><p>בורסת העיר: מבנה ותפקיד</p></div>
    </div>
    <div class="slide-rule"></div><div class="slide-mark"></div>
  </section>

  <section class="slide c-indices">
    <svg class="curve-panel" width="200" height="290" viewBox="0 0 200 290" aria-hidden="true">
      <defs><linearGradient id="curveFillA" x1="0" y1="0" x2="0" y2="1">
        <stop offset="0" stop-color="var(--blue-deep)"/><stop offset="1" stop-color="var(--blue-light)"/></linearGradient></defs>
      <path d="M30,0 H200 V290 H140 C60,270 40,200 40,150 C40,90 60,50 30,0 Z" fill="url(#curveFillA)"/>
    </svg>
    <h2 class="curve-title">מדדים</h2>
    <div class="chev" style="right:164px;top:54px"></div>
    <div class="chev" style="right:158px;top:112px"></div>
    <div class="chev" style="right:160px;top:170px"></div>
    <div class="chev" style="right:176px;top:224px"></div>
    <div class="index-item" style="right:208px;top:227px">איך קונים מדד (תעודות סל)</div>
    <div class="slide-rule"></div><div class="slide-mark"></div>
  </section>

  <section class="slide title-slide c-hero">
    <div class="market-photo" role="img" aria-label="תמונת רקע של מסכי מסחר ונתוני בורסה בגווני כחול"></div>
    <div class="brand-tab">
      <div class="brand-dot"></div>
      <div class="brand-name">מועדון הצמיחה</div>
      <div class="brand-sub">של דן לוי</div>
    </div>
    <h1 class="course-title">קורס שוק ההון- בסיס (חדש)</h1>
    <div class="presenter-pill">נועה כהן</div>
  </section>
</div>

<section class="slide title-slide g1">
  <div class="market-photo" role="img" aria-label="תמונת רקע של מסכי מסחר ונתוני בורסה בגווני כחול"></div>
  <div class="brand-tab">
    <div class="brand-dot"></div>
    <div class="brand-name">מועדון הצמיחה</div>
    <div class="brand-sub">של דן לוי</div>
  </div>
  <h1 class="course-title">קורס שוק ההון- בסיס (חדש)</h1>
  <div class="presenter-pill">נועה כהן</div>
</section>

<section class="slide g2">
  <div class="side-panel">
    <div class="portrait" role="img" aria-label="צללית של המרצה על רקע כחול"></div>
    <h2 class="panel-title">רקע על<br>המרצה</h2>
  </div>
  <ul class="bio-list">
    <li><span class="bio-icon"><svg width="10" height="10" viewBox="0 0 10 10"><path d="M2 5l2 2 4-4" stroke="#fff" stroke-width="1.6" fill="none"/></svg></span>בעל שני תארים במנהל עסקים</li>
    <li><span class="bio-icon"><svg width="10" height="10" viewBox="0 0 10 10"><path d="M2 5l2 2 4-4" stroke="#fff" stroke-width="1.6" fill="none"/></svg></span>מרצה במכללה לכלכלה</li>
    <li><span class="bio-icon"><svg width="10" height="10" viewBox="0 0 10 10"><path d="M2 5l2 2 4-4" stroke="#fff" stroke-width="1.6" fill="none"/></svg></span>יזם הייטק בתחום הפינטק</li>
    <li><span class="bio-icon"><svg width="10" height="10" viewBox="0 0 10 10"><path d="M2 5l2 2 4-4" stroke="#fff" stroke-width="1.6" fill="none"/></svg></span>כותב טורי דעה בנושאי כלכלה</li>
    <li><span class="bio-icon"><svg width="10" height="10" viewBox="0 0 10 10"><path d="M2 5l2 2 4-4" stroke="#fff" stroke-width="1.6" fill="none"/></svg></span>הקים וניהל חברה למסחר בנגזרים פיננסים</li>
  </ul>
  <div class="slide-rule"></div><div class="slide-mark"></div><span class="slide-num">2</span>
</section>

<section class="slide g3">
  <div class="top-band"><h2 class="band-title">בורסה</h2></div>
  <div class="topic-grid">
    <div class="topic-card"><span class="num">01</span><p>מה זו בורסה?</p></div>
    <div class="topic-card"><span class="num">02</span><p>ההיסטוריה של הבורסה</p></div>
    <div class="topic-card"><span class="num">03</span><p>הקבוצות הציבוריות והמוסדות</p></div>
    <div class="topic-card"><span class="num">04</span><p>ההבדל בין שוק ראשוני לשוק משני</p></div>
    <div class="topic-card"><span class="num">05</span><p>איך הבורסה משפיעה על הכלכלה?</p></div>
    <div class="topic-card"><span class="num">06</span><p>בורסת העיר: מבנה ותפקיד</p></div>
  </div>
  <div class="slide-rule"></div><div class="slide-mark"></div><span class="slide-num">3</span>
</section>

<section class="slide g4">
  <h2 class="center-title">ני"ע נסחרים בבורסה</h2>
  <svg class="securities-chart" width="170" height="170" viewBox="-85 -85 170 170" aria-hidden="true">
    <g fill="var(--blue-deep)" stroke="#fff" stroke-width="3">
      <path d="M0,-80 A80,80 0 0 1 76.1,-24.7 L20.9,-6.8 A22,22 0 0 0 0,-22 Z"/>
      <path d="M76.1,-24.7 A80,80 0 0 1 47,64.7 L12.9,17.8 A22,22 0 0 0 20.9,-6.8 Z"/>
      <path d="M47,64.7 A80,80 0 0 1 -47,64.7 L-12.9,17.8 A22,22 0 0 0 12.9,17.8 Z"/>
      <path d="M-47,64.7 A80,80 0 0 1 -76.1,-24.7 L-20.9,-6.8 A22,22 0 0 0 -12.9,17.8 Z"/>
      <path d="M-76.1,-24.7 A80,80 0 0 1 0,-80 L0,-22 A22,22 0 0 0 -20.9,-6.8 Z"/>
    </g>
    <circle r="20" fill="#fff"/>
    <g stroke="#fff" stroke-width="2" fill="none">
      <path d="M22,-52 l8,-8 l6,5 l10,-12"/>
      <rect x="40" y="10" width="14" height="16" rx="2"/>
      <path d="M-6,46 h12 M0,40 v12 M-4,42 l8,8 M4,42 l-8,8"/>
      <rect x="-56" y="12" width="14" height="12" rx="2"/>
      <path d="M-44,-52 h14 v12 h-14 z M-44,-46 h14"/>
    </g>
  </svg>
  <div class="sec-label" style="right:24px;top:70px">מניות</div>
  <div class="sec-label" style="right:24px;top:150px">אג"חים</div>
  <div class="sec-label" style="right:215px;top:262px;text-align:center">תעודות סל</div>
  <div class="sec-label" style="left:24px;top:182px;text-align:left">קרנות נאמנות</div>
  <div class="sec-label" style="left:24px;top:70px;text-align:left">נגזרים פיננסים</div>
  <div class="slide-rule"></div><div class="slide-mark"></div><span class="slide-num">4</span>
</section>

<section class="slide g5">
  <svg class="curve-panel" width="200" height="290" viewBox="0 0 200 290" aria-hidden="true">
    <defs><linearGradient id="curveFillB" x1="0" y1="0" x2="0" y2="1">
      <stop offset="0" stop-color="var(--blue-deep)"/><stop offset="1" stop-color="var(--blue-light)"/></linearGradient></defs>
    <path d="M30,0 H200 V290 H140 C60,270 40,200 40,150 C40,90 60,50 30,0 Z" fill="url(#curveFillB)"/>
  </svg>
  <h2 class="curve-title">מדדים</h2>
  <div class="chev" style="right:164px;top:54px"><svg width="8" height="8" viewBox="0 0 8 8"><path d="M5.5 1L2.5 4l3 3" stroke="var(--blue)" stroke-width="1.6" fill="none"/></svg></div>
  <div class="index-item" style="right:196px;top:52px">המדדים העיקריים בעולם (צפון 500, הגשר, טק-100)</div>
  <div class="chev" style="right:158px;top:112px"><svg width="8" height="8" viewBox="0 0 8 8"><path d="M5.5 1L2.5 4l3 3" stroke="var(--blue)" stroke-width="1.6" fill="none"/></svg></div>
  <div class="index-item" style="right:190px;top:110px">המדדים העיקריים בישראל (מרכז 35, מרכז 90, מרכז 125)</div>
  <div class="chev" style="right:160px;top:170px"><svg width="8" height="8" viewBox="0 0 8 8"><path d="M5.5 1L2.5 4l3 3" stroke="var(--blue)" stroke-width="1.6" fill="none"/></svg></div>
  <div class="index-item" style="right:192px;top:173px">איך מחשבים מדד</div>
  <div class="chev" style="right:176px;top:224px"><svg width="8" height="8" viewBox="0 0 8 8"><path d="M5.5 1L2.5 4l3 3" stroke="var(--blue)" stroke-width="1.6" fill="none"/></svg></div>
  <div class="index-item" style="right:208px;top:227px">איך קונים מדד (תעודות סל)</div>
  <div class="slide-rule"></div><div class="slide-mark"></div><span class="slide-num">5</span>
</section>

</body>
</html>
```